Hotel Business Card Project

Amber Crest Hotel will be a premium boutique hotel in Dhaka, Bangladesh. The hotel will offer the finest amenities and facilities available on the market, and the cost per room investment will far exceed other 5-star hotels currently in the market.

As a result, we wanted the business card to reflect that premium/luxurious/upscale feel, and also be elegant and hospitable at the same time.

The name 'Amber Crest' is derived from the fact that Bangladesh has 6 distinct seasons (you can get more information online if required, or contact me about it). The leaves in the logo has the tree because trees give people shade, protection and safety (just like our hotel would try to give).

Target Market(s)

Business professionals, guests

Industry/Entity Type

Investment

Requirements
Must have
• Elegant, Classy and very attractive business card.

Must be editable to enter specific Names, Positions, Phone numbers and email later on.
Nice to have
• The address would be: House 47, Road 23, Lakeview 5, Dhaka 1208, Bangladesh

Slogan- Luxury Redefined

```html
<!DOCTYPE html>
<html lang="en">
<head>
<meta charset="utf-8">
<title>Amber Crest Hotel – Business Card</title>
<link rel="stylesheet" href="https://fonts.googleapis.com/css2?family=PT+Sans:ital,wght@0,400;0,700;1,400&family=Pinyon+Script&display=swap">
<style>
  :root {
    --card-bg: #ffffff;
    --leaf-fill: #f1f0ee;
    --ink: #231f20;
    --brand-ink: #5b5b5b;
    --rule: #2b2b2b;
  }
  html, body {
    margin: 0;
    padding: 0;
    width: 1200px;
    height: 672px;
    overflow: hidden;
    background: var(--card-bg);
  }
  .card {
    position: relative;
    width: 1200px;
    height: 672px;
    overflow: hidden;
    background: var(--card-bg);
    font-family: "PT Sans", "Myriad Pro", Arial, sans-serif;
    color: var(--ink);
  }
  .leaf-backdrop {
    position: absolute;
    inset: 0;
    width: 1200px;
    height: 672px;
  }
  .leaf-backdrop path { fill: var(--leaf-fill); }

  .brand-name {
    position: absolute;
    left: 52px;
    top: 200px;
    margin: 0;
    font-family: "PT Sans", Arial, sans-serif;
    font-weight: 400;
    font-size: 36px;
    line-height: 44px;
    letter-spacing: 0.5px;
    color: var(--brand-ink);
    white-space: nowrap;
  }

  .slogan {
    position: absolute;
    right: 40px;
    top: 22px;
    margin: 0;
    font-family: "Pinyon Script", cursive;
    font-weight: 400;
    font-size: 58px;
    line-height: 80px;
    color: var(--ink);
    white-space: nowrap;
  }

  .holder {
    position: absolute;
    left: 466px;
    top: 270px;
    width: 626px;
  }
  .holder-name {
    margin: 0;
    font-weight: 700;
    font-size: 44px;
    line-height: 50px;
  }
  .holder-position {
    margin: 2px 0 0;
    font-style: italic;
    font-size: 36px;
    line-height: 46px;
  }
  .holder-rule {
    position: absolute;
    left: -3px;
    top: 102px;
    width: 629px;
    height: 0;
    border: 0;
    border-top: 2px solid var(--rule);
    margin: 0;
  }

  .contact {
    position: absolute;
    left: 466px;
    top: 395px;
    margin: 0;
    font-size: 36px;
    line-height: 46px;
    font-style: normal;
    white-space: nowrap;
  }
  .address {
    position: absolute;
    left: 466px;
    top: 553px;
    margin: 0;
    font-size: 36px;
    line-height: 42px;
    font-style: normal;
    white-space: nowrap;
  }
  .contact p, .address p { margin: 0; }
</style>
</head>
<body>
  <main class="card">
    <svg class="leaf-backdrop" viewBox="0 0 1200 672" aria-hidden="true">
      <path d="M76 636 C190 420 520 150 1000 118 C1080 113 1150 118 1200 126 L1200 672 L132 672 C100 660 82 650 76 636 Z"/>
    </svg>

    <p class="brand-name">Amber Crest Hotel</p>

    <p class="slogan">Luxury Redefined</p>

    <section class="holder">
      <h1 class="holder-name">Your Name</h1>
      <p class="holder-position">Position</p>
      <hr class="holder-rule">
    </section>

    <address class="contact">
      <p>Contact no.: 02 555 0142</p>
      <p>Mobile: +880 1712 345678</p>
      <p>Email: name@ambercrest.com</p>
    </address>

    <address class="address">
      <p>House 47, Road 23, Lakeview 5</p>
      <p>Dhaka 1208, Bangladesh</p>
    </address>
  </main>
</body>
</html>
```